Kraft Eco-friendly pouch back imprint

Updating the design imprint on the back of our eco-friendly kraft stand up pouches. The current package back is a story letter but we want to change it to be more visually eye catching and make better use of buzzwords and graphics. I've uploaded a PDF with the current graphic so that key buzz words and thoughts could be pulled and highlighted.

The printing will be done in black and white, so don't spend time with colors. The imprint area is approximately 7" high x 5" wide.

I definitely want our logo at the top of the package, and I'm attaching two options.

Our mission is to be the Healthiest Pet Bakery in the U.S. That needs to be another point of emphasis.

Other potential buzzwords or bullets include:
Artisan Recipes
Simple Ingredients
No corn, wheat, soy, GMOs, or preservatives
Handcrafted
Locally sourced (Pacific NW)
Eco-conscious company
Updates

The system only allowed 24 hours. That is a ridiculously short time window.

Target Market(s)

Pet parents seeking natural, healthy products

Industry/Entity Type

independent pet channel

Colors

Designer to choose only greyscale colors for use in the design.

Requirements
Must have
• Logo, Mission, buzz words, graphics

```html
<!DOCTYPE html>
<html lang="en">
<head>
<meta charset="utf-8">
<title>Whisker Hearth Bakery – Pouch Back Imprint</title>
<link rel="stylesheet" href="https://fonts.googleapis.com/css2?family=Crimson+Text:wght@400;600;700&family=Poppins:wght@500;600&display=swap">
<style>
  :root {
    --page: #e9e9e9;
    --ink: #111111;
    --paper-light: #f2f2f2;
    --paper-mid: #bdbdbd;
    --paper-dark: #8c8c8c;
    --panel-grey: #a9a9a9;
    --white: #ffffff;
  }
  * { margin: 0; padding: 0; box-sizing: border-box; }
  html, body { width: 1200px; height: 799px; overflow: hidden; background: var(--page); }
  .label {
    position: absolute; left: 331px; top: 20px; width: 538px; height: 760px;
    background: linear-gradient(100deg, var(--paper-light) 0%, var(--paper-mid) 55%, var(--paper-dark) 100%);
    overflow: hidden; color: var(--ink);
    font-family: "Crimson Text", serif;
  }
  .label__waves { position: absolute; inset: 0; }
  .brand {
    position: absolute; left: 52px; top: 92px; width: 220px;
    display: flex; align-items: center; gap: 10px;
    font-family: "Crimson Text", serif; font-weight: 700; font-size: 26px; line-height: 1.05;
    color: var(--ink);
  }
  .brand__dot { width: 26px; height: 26px; border-radius: 50%; background: var(--ink); flex: none; }
  .seal {
    position: absolute; left: 340px; top: 17px; width: 168px; height: 168px; border-radius: 50%;
    background: radial-gradient(circle, #5a5a5a 0%, #2a2a2a 60%, #d8d8d8 61%, #d8d8d8 70%, #1a1a1a 71%);
  }
  .story { position: absolute; left: 49px; top: 270px; width: 268px; }
  .story__title { font-size: 17.5px; font-weight: 700; margin-bottom: 3px; }
  .story__text { font-size: 11.2px; line-height: 14.8px; }
  .story__ingredients { margin-top: 14px; }
  .story__ingredients strong { font-size: 14px; font-weight: 700; }
  .benefits {
    position: absolute; left: 349px; top: 262px; width: 146px; height: 232px;
    border: 2px solid var(--ink); border-radius: 12px; background: var(--panel-grey);
    font-family: "Poppins", sans-serif; overflow: hidden;
  }
  .benefits__head {
    background: var(--ink); color: var(--white); text-align: center;
    font-size: 17px; font-weight: 500; line-height: 21px; padding: 10px 4px 9px;
  }
  .benefits__list { list-style: none; padding: 12px 0 0 16px; }
  .benefits__item { display: flex; gap: 9px; align-items: flex-start; margin-bottom: 10px; font-size: 13.5px; line-height: 14px; font-weight: 500; }
  .benefits__item small { display: block; font-size: 11px; margin-top: 3px; }
  .benefits__icon { width: 16px; height: 16px; margin-top: 6px; flex: none; }
  .free-badges { position: absolute; left: 64px; top: 526px; display: flex; gap: 17px; }
  .free-badge {
    width: 70px; height: 70px; border-radius: 50%; background: var(--ink);
    border: 3px solid #4a4a4a; box-shadow: 0 0 0 2px var(--ink);
    color: var(--white); font-family: "Poppins", sans-serif; font-weight: 500;
    display: flex; flex-direction: column; justify-content: center; align-items: center;
    font-size: 12.5px; line-height: 13px; text-align: center;
  }
  .free-badge--small { font-size: 10.5px; }
  .maker {
    position: absolute; left: 242px; top: 620px; width: 259px; height: 129px;
    background: var(--ink); color: var(--white);
  }
  .maker__top {
    position: absolute; left: 10px; top: 11px; width: 242px; height: 48px;
    background: var(--white); color: var(--ink); display: flex;
  }
  .maker__address {
    width: 126px; padding: 3px 4px; border: 1.5px solid var(--ink);
    font-size: 10.5px; line-height: 14px; color: #333;
  }
  .maker__eco { display: flex; align-items: center; gap: 6px; padding-left: 6px;
    font-family: "Poppins", sans-serif; font-weight: 600; font-size: 8.5px; line-height: 9.5px; }
  .maker__eco-mark { width: 26px; height: 26px; border: 1.5px solid var(--ink); }
  .maker__contacts { position: absolute; left: 24px; top: 69px; list-style: none; font-size: 11px; line-height: 21px; }
  .maker__contacts li { display: flex; align-items: center; gap: 12px; }
  .maker__contacts svg { width: 12px; height: 12px; }
</style>
</head>
<body>
<main class="label">
  <svg class="label__waves" viewBox="0 0 538 760" aria-hidden="true">
    <path d="M0 0 H270 C300 40 330 90 320 160 C300 250 240 290 300 330 C360 370 420 380 380 460 C340 520 220 500 170 560 C120 620 60 700 0 720 Z" fill="#f5f5f5" opacity="0.75"/>
    <path d="M270 0 C330 60 330 120 350 190 C370 250 420 290 410 340" fill="none" stroke="#7a7a7a" stroke-width="1.5"/>
    <path d="M0 540 C80 500 180 470 260 430 C330 400 420 420 538 380" fill="none" stroke="#7a7a7a" stroke-width="1.5"/>
    <path d="M0 760 V640 C120 610 260 560 400 520 C460 505 500 510 538 500 V760 Z" fill="#9a9a9a" opacity="0.35"/>
  </svg>

  <div class="brand"><span class="brand__dot"></span><span>Whisker Hearth Bakery</span></div>

  <div class="seal" role="img" aria-label="Round bakery seal with pet mascot"></div>

  <section class="story">
    <h2 class="story__title">Healthy treats your pet will love!</h2>
    <p class="story__text">Lorem ipsum dolor sit amet, consectetur adipiscing elit. Morbi ultricies molestie orci. Aenean purus mauris, sodales nec diam dignissim, porttitor laoreet enim. Aliquam id sollicitudin turpis. Vivamus aliquet elit sem, et ornare ex aliquam in. In cursus, felis non pretium molestie, tellus lacus facilisis metus, ut accumsan nisi nulla accumsan risus.</p>
    <p class="story__text story__ingredients"><strong>Ingredients:</strong> Etiam id pharetra ante. Nunc sit amet ante id justo consequat tempor. Nullam pretium arcu eu hendrerit aliquam. Sed in purus eros.</p>
  </section>

  <aside class="benefits">
    <h3 class="benefits__head">For happy, healthy pets!</h3>
    <ul class="benefits__list">
      <li class="benefits__item"><svg class="benefits__icon" viewBox="0 0 16 16"><circle cx="8" cy="10" r="4"/><circle cx="3" cy="5" r="1.8"/><circle cx="6.5" cy="2.5" r="1.8"/><circle cx="10" cy="2.5" r="1.8"/><circle cx="13.5" cy="5" r="1.8"/></svg><span>Artisan Recipes</span></li>
      <li class="benefits__item"><svg class="benefits__icon" viewBox="0 0 16 16"><circle cx="8" cy="10" r="4"/><circle cx="3" cy="5" r="1.8"/><circle cx="6.5" cy="2.5" r="1.8"/><circle cx="10" cy="2.5" r="1.8"/><circle cx="13.5" cy="5" r="1.8"/></svg><span>Simple Ingredients</span></li>
      <li class="benefits__item"><svg class="benefits__icon" viewBox="0 0 16 16"><circle cx="8" cy="10" r="4"/><circle cx="3" cy="5" r="1.8"/><circle cx="6.5" cy="2.5" r="1.8"/><circle cx="10" cy="2.5" r="1.8"/><circle cx="13.5" cy="5" r="1.8"/></svg><span>Locally Sourced<small>(Pacific NW)</small></span></li>
    </ul>
  </aside>

  <div class="free-badges">
    <div class="free-badge"><span>SOY</span><span>free</span></div>
    <div class="free-badge"><span>GMO</span><span>free</span></div>
    <div class="free-badge free-badge--small"><span>PARABEN</span><span>free</span></div>
    <div class="free-badge"><span>CORN</span><span>free</span></div>
    <div class="free-badge"><span>WHEAT</span><span>free</span></div>
  </div>

  <footer class="maker">
    <div class="maker__top">
      <p class="maker__address">Manufactured by<br>Whisker Hearth Bakery<br>Cedar Cove, WA</p>
      <div class="maker__eco"><span class="maker__eco-mark"></span><span>AN<br>ECO-CONSCIOUS<br>COMPANY</span></div>
    </div>
    <ul class="maker__contacts">
      <li><svg viewBox="0 0 12 12" fill="none" stroke="#fff" stroke-width="1"><circle cx="6" cy="6" r="5"/><ellipse cx="6" cy="6" rx="2.2" ry="5"/><path d="M1 6h10"/></svg>www.whiskerhearthbakery.com</li>
      <li><svg viewBox="0 0 12 12"><circle cx="6" cy="6" r="6" fill="#fff"/><path d="M4 3l1 1.5-.7.8a4 4 0 0 0 2.4 2.4l.8-.7L9 8l-.8 1A5 5 0 0 1 3 3.8z" fill="#111"/></svg>(0113)555-0142</li>
    </ul>
  </footer>
</main>
</body>
</html>
```